Private Investigator needs business card with an intelligent logo

Private Investigator needs uncluttered, intelligently designed business card with simple logo. Prefer one or two colour print only. Must convey serious approach with only basic information: Business Name, "Clearmarsh Investigations"
Phone: 03 5550 1946 Email: info@clearmarsh.com.au Web: www.clearmarsh.com.au
Agents Name: Derek Hollins Title: Investigator Mobile: 0491 570 156

Thank you all very much for your designs.  There was some really excellent ideas and the choice was very hard.  I sought opinions from a number of people about which was the best one and there were a number of different choices but eventually the majority went with one design from Kavlorix.  Thank you especially to those designers that made some changes when I suggested them.

Thanks again for all your efforts and good luck with your design careers.  I will certainly use Graftnest again with the great quality of designers that made submissions.

Regards  Derek Hollins

```html
<!DOCTYPE html>
<html lang="en">
<head>
<meta charset="utf-8">
<title>Clearmarsh Investigations – Business Card</title>
<link rel="stylesheet" href="https://fonts.googleapis.com/css2?family=Cinzel:wght@400&family=Crimson+Text:wght@400;700&display=swap">
<style>
  :root {
    --backdrop: #d9d9d9;
    --card: #ffffff;
    --ink: #111111;
    --ink-soft: #2a2a2a;
    --print-tone: #1a1a1a;
  }
  * { margin: 0; padding: 0; box-sizing: border-box; }
  html, body {
    width: 1200px;
    height: 1000px;
    overflow: hidden;
    background: var(--backdrop);
  }
  .card {
    position: absolute;
    left: 150px;
    top: 243px;
    width: 900px;
    height: 514px;
    background: var(--card);
    color: var(--ink);
    box-shadow: 0 6px 24px rgba(0,0,0,0.18);
  }
  .business-name {
    position: absolute;
    left: 70px;
    top: 62px;
    font-family: "Cinzel", serif;
    font-size: 38px;
    letter-spacing: 1px;
    color: var(--ink-soft);
    white-space: nowrap;
  }
  .business-name .dot { font-size: 28px; vertical-align: middle; margin: 0 14px; }
  .divider {
    position: absolute;
    left: 0;
    top: 180px;
    width: 560px;
    height: 22px;
  }
  .agent {
    position: absolute;
    right: 92px;
    top: 140px;
    text-align: right;
    font-family: "Crimson Text", serif;
  }
  .agent-name { font-size: 44px; font-weight: 700; line-height: 1; }
  .agent-title { font-size: 22px; line-height: 1.1; margin-top: 2px; }
  .contact {
    position: absolute;
    right: 92px;
    top: 275px;
    text-align: right;
    font-family: "Crimson Text", serif;
    font-size: 25px;
    line-height: 1.32;
    letter-spacing: 0.5px;
  }
  .print-mark {
    position: absolute;
    left: 58px;
    top: 295px;
    width: 100px;
    height: 150px;
    border-radius: 50% 50% 46% 46% / 42% 42% 58% 58%;
    background: radial-gradient(ellipse at 50% 45%, #555 0%, var(--print-tone) 70%);
  }
</style>
</head>
<body>
  <article class="card">
    <h1 class="business-name"><span class="dot">•</span>Clearmarsh Investigations<span class="dot">•</span></h1>

    <svg class="divider" viewBox="0 0 560 22" aria-hidden="true">
      <polygon points="0,16 560,2 560,12 0,20" fill="var(--ink)"/>
    </svg>

    <div class="agent">
      <p class="agent-name">Derek Hollins</p>
      <p class="agent-title">Investigator</p>
    </div>

    <div class="contact">
      <p>Mobile: 0491 570 156</p>
      <p>Phone: 03 5550 1946</p>
      <p>Email: info@clearmarsh.com.au</p>
      <p>Web: www.clearmarsh.com.au</p>
    </div>

    <div class="print-mark" role="img" aria-label="Fingerprint illustration"></div>
  </article>
</body>
</html>
```